A boutique/architectural website for a landscape company

I'm after a minimilstic boutique website for my landscape design and construction business. I have been exploring Wix and created some pages on that but want something more aesthetic.

Industry/Entity Type

Landscaping design and construction

Number of Pages Required

5+ page

Font styles to use
Sans Serif

Colors

Designer to choose colors to be used in the design.

Requirements
Must have
• an architectural, minimalistic look
Nice to have
• Simplicitly and nice images
Should not have
• A corporate look

```html
<!DOCTYPE html>
<html lang="en">
<head>
<meta charset="utf-8">
<title>Wattle Landscaping</title>
<link href="https://fonts.googleapis.com/css2?family=Montserrat:wght@500;600&family=Roboto:wght@400;500;700&family=Playfair+Display:wght@700&display=swap" rel="stylesheet">
<style>
:root{
  --sage:#c9d5c1;
  --forest:#0b3d35;
  --forest-deep:#093731;
  --ink:#1c2622;
  --muted:#7a7f7c;
  --white:#ffffff;
}
*{margin:0;padding:0;box-sizing:border-box}
html,body{width:1200px;height:3367px;overflow:hidden}
body{position:relative;background:var(--white);font-family:"Roboto",Arial,sans-serif;color:var(--ink)}
.abs{position:absolute}
.photo{position:absolute}
.heading{position:absolute;left:0;width:1200px;text-align:center;font-family:"Montserrat",Arial,sans-serif;font-weight:600;font-size:37px;color:var(--forest);letter-spacing:.5px}

/* hero */
.hero-left{left:0;top:0;width:668px;height:660px;background:var(--sage)}
.hero-right{left:668px;top:0;width:532px;height:660px;background:var(--forest)}
.hero-frame{left:669px;top:49px;width:485px;height:563px;border:1px solid rgba(255,255,255,.15)}
.brand{left:100px;top:20px;width:96px;text-align:center;font-family:"Montserrat",Arial,sans-serif;font-weight:600;font-size:13px;letter-spacing:4px;color:var(--forest)}
.brand .mark{display:block;width:26px;height:26px;margin:0 auto 8px;border-radius:50%;background:var(--forest)}
.nav{left:256px;top:34px;display:flex;gap:23px;font-size:15px;font-weight:500;color:var(--ink)}
.nav .active{color:#2e6d5e}
.hero-photo{left:111px;top:88px;width:730px;height:485px;background:linear-gradient(180deg,#6f8fb6 0%,#3f5a48 40%,#3f4f5e 60%,#4e7a3a 85%,#3b5f2c 100%)}
.play{left:80px;top:445px;width:86px;height:56px;border-radius:28px;background:var(--forest);display:flex;align-items:center;justify-content:center}
.play-label{left:179px;top:465px;font-size:11px;font-weight:500;color:var(--white)}
.play-line{left:222px;top:472px;width:24px;height:2px;background:var(--white)}
.hero-title{left:111px;top:476px;width:730px;text-align:center;font-family:"Montserrat",Arial,sans-serif;font-weight:500;font-size:38px;color:var(--white)}
.social{top:101px;font-size:10px;font-weight:500;color:var(--white)}
.arrow{width:44px;height:44px;border-radius:50%;background:#145247;display:flex;align-items:center;justify-content:center;left:975px}
.slide-no{left:960px;top:325px;font-family:"Playfair Display",Georgia,serif;font-weight:700;font-size:66px;font-variant-numeric:lining-nums;color:var(--white)}
.hero-text{left:796px;top:462px;width:332px;font-size:15px;font-weight:500;line-height:24px;color:var(--white)}

/* about */
.lead{left:165px;top:788px;width:870px;text-align:center;font-size:14px;line-height:26px;color:var(--muted)}

/* services */
.services{left:0;top:1239px;width:1200px;height:533px;background:var(--sage)}
.svc-title{top:1404px;font-size:22px;font-weight:700;color:var(--ink)}
.svc-icon{width:98px;height:98px;border-radius:50%;background:var(--forest);border:3px solid #6f8f83;display:flex;align-items:center;justify-content:center}
.svc-text{top:1483px;width:430px;font-size:14px;line-height:25.7px;color:var(--muted)}
.divider{left:600px;top:1380px;width:1px;height:262px;background:rgba(11,61,53,.15)}
.btn-start{left:506px;top:1670px;width:188px;height:47px;border-radius:24px;background:var(--forest);color:var(--white);font-weight:700;font-size:16px;display:flex;align-items:center;justify-content:center;gap:8px}

/* footer */
.footer{left:0;top:3008px;width:1200px;height:359px;background:var(--forest-deep)}
.f-brand{left:120px;top:3140px;width:170px;text-align:center;font-family:"Montserrat",Arial,sans-serif;font-weight:500;font-size:26px;letter-spacing:9px;color:var(--white)}
.f-brand .mark{display:block;width:46px;height:46px;border-radius:50%;background:var(--white);margin:0 auto 22px}
.f-social{top:3245px;width:14px;height:14px;border-radius:50%;border:2px solid var(--white)}
.f-head{top:3072px;font-size:16px;font-weight:700;color:var(--white)}
.f-item{font-size:13px;line-height:17px;color:var(--white)}
.f-item b{display:block;font-size:11px;font-weight:700}
.f-links{left:672px;top:3117px;font-size:13px;line-height:26px;color:var(--white)}
.f-note{left:862px;top:3116px;width:240px;font-size:12px;line-height:18.5px;color:var(--white)}
.btn-quote{left:862px;top:3200px;width:199px;height:40px;border-radius:20px;background:var(--white);color:var(--forest);font-weight:700;font-size:14px;display:flex;align-items:center;justify-content:center}
.go-up{left:1007px;top:3280px;width:81px;height:19px;border-radius:10px;background:var(--forest);border:1px solid #2b6358;font-size:10px;font-weight:700;color:var(--white);display:flex;align-items:center;justify-content:center;gap:4px}
.f-rule{left:111px;top:3304px;width:977px;height:1px;background:rgba(255,255,255,.15)}
.copy{left:111px;top:3325px;font-size:13px;color:var(--white)}
.legal{right:112px;top:3325px;font-size:13px;color:var(--white)}
</style>
</head>
<body>

<!-- hero -->
<div class="abs hero-left"></div>
<div class="abs hero-right"></div>
<div class="abs hero-frame"></div>
<div class="abs brand"><span class="mark"></span>WATTLE</div>
<nav class="abs nav"><span class="active">Home</span><span>About Us</span><span>Services</span><span>Gallery</span><span>Contact Us</span></nav>
<div class="photo hero-photo" role="img" aria-label="Two-storey blue house at dusk with lit windows, lawn, young tree and tall pines"></div>
<div class="abs play"><svg width="24" height="24" viewBox="0 0 24 24"><path d="M5 2 L22 12 L5 22 Z" fill="#fff"/></svg></div>
<div class="abs play-label">PLAY</div>
<div class="abs play-line"></div>
<div class="abs hero-title">WATTLE LANDSCAPING</div>
<div class="abs social" style="left:935px">Journal</div>
<div class="abs social" style="left:1012px">Studio</div>
<div class="abs arrow" style="top:187px"><svg width="14" height="14" viewBox="0 0 14 14"><path d="M9 2 L4 7 L9 12" stroke="#fff" stroke-width="2.2" fill="none"/></svg></div>
<div class="abs arrow" style="top:238px"><svg width="14" height="14" viewBox="0 0 14 14"><path d="M5 2 L10 7 L5 12" stroke="#fff" stroke-width="2.2" fill="none"/></svg></div>
<div class="abs slide-no">01</div>
<p class="abs hero-text">Sed ut perspiciatis unde omnis iste natus error sit voluptatem accusantium doloremque laudantium, totam aperiam,</p>

<!-- about -->
<h2 class="heading" style="top:730px">ABOUT US</h2>
<p class="abs lead">Lorem ipsum dolor sit amet, consectetur adipiscing elit, sed do eiusmod tempor incididunt ut labore et dolore magna aliqua. Ut enim ad minim veniam, quis nostrud exercitation ullamco laboris nisi ut aliquip ex ea commodo consequat. Duis aute irure dolor in reprehenderit in voluptate velit esse cillum dolore eu fugiat nulla pariatur. Excepteur sint occaecat cupidatat non proident, sunt in culpa qui officia deserunt mollit anim id est laborum.</p>
<div class="photo" style="left:111px;top:929px;width:315px;height:216px;background:linear-gradient(135deg,#6aa03a,#3f7a26 60%,#b9a98a)" role="img" aria-label="Aerial view of a gardener mowing a lawn beside a stepping-stone path"></div>
<div class="photo" style="left:442px;top:929px;width:315px;height:216px;background:linear-gradient(180deg,#1f2e2a,#3b3a30 55%,#1f6e8c 80%,#203a22)" role="img" aria-label="Modern house at night with lit pool and garden"></div>
<div class="photo" style="left:773px;top:929px;width:315px;height:216px;background:linear-gradient(135deg,#c9ccce,#9ea3a6 60%,#6f8f4a)" role="img" aria-label="Grey paved driveway edged with gravel and round shrubs"></div>

<!-- services -->
<div class="abs services"></div>
<h2 class="heading" style="top:1291px">OUR SERVICES</h2>
<div class="abs svc-title" style="left:218px">LANDSCAPE DESIGN</div>
<div class="abs svc-icon" style="left:463px;top:1369px"><svg width="50" height="50" viewBox="0 0 50 50" fill="none" stroke="#fff" stroke-width="2"><path d="M6 30 Q25 22 44 30"/><path d="M6 37 Q25 29 44 37"/><path d="M10 44 Q25 36 40 44"/><circle cx="18" cy="15" r="5"/><path d="M18 20 V26"/><path d="M30 24 L34 12 L38 24 Z"/></svg></div>
<p class="abs svc-text" style="left:131px;text-align:right">Lorem ipsum dolor sit amet, consectetur adipiscing elit, sed do eiusmod tempor incididunt ut labore et dolore magna aliqua. Ut enim ad minim veniam, quis nostrud exercitation ullamco laboris nisi ut aliquip ex ea commodo consequat. Duis aute irure dolor in reprehenderit in voluptate velit esse cillum dolore eu fugiat nulla Excepteur sint occaecat pariatur.</p>
<div class="abs divider"></div>
<div class="abs svc-icon" style="left:638px;top:1369px"><svg width="50" height="50" viewBox="0 0 50 50" fill="none" stroke="#fff" stroke-width="2"><path d="M30 44 V10"/><path d="M16 10 H44"/><path d="M40 10 V18"/><rect x="8" y="24" width="14" height="20"/><path d="M12 29 H18 M12 34 H18 M12 39 H18"/><path d="M4 44 H46"/></svg></div>
<div class="abs svc-title" style="left:771px">CONSTRUCTION BUSINESS</div>
<p class="abs svc-text" style="left:638px">Lorem ipsum dolor sit amet, consectetur adipiscing elit, sed do eiusmod tempor incididunt ut labore et dolore magna aliqua. Ut enim ad minim veniam, quis nostrud exercitation ullamco laboris nisi ut aliquip ex ea commodo consequat. Duis aute irure dolor in reprehenderit in voluptate velit esse cillum dolore eu fugiat nulla Excepteur sint occaecat pariatur.</p>
<div class="abs btn-start">GET STARTED <svg width="16" height="16" viewBox="0 0 16 16"><circle cx="8" cy="8" r="8" fill="#fff"/><path d="M6.5 4.5 L10 8 L6.5 11.5" stroke="#0b3d35" stroke-width="2" fill="none"/></svg></div>

<!-- portfolio -->
<h2 class="heading" style="top:1856px">OUR PORFOLIO</h2>
<div class="photo" style="left:111px;top:1936px;width:311px;height:409px;background:linear-gradient(180deg,#5d8fd0,#dcd1b4 45%,#b39f7c 75%,#4e7a32)" role="img" aria-label="Cream two-storey house with stone planter and lawn"></div>
<div class="photo" style="left:111px;top:2364px;width:311px;height:408px;background:linear-gradient(135deg,#cfc6bd,#b9aea1 50%,#6b8a4d)" role="img" aria-label="Worker laying turf beside paving"></div>
<div class="photo" style="left:445px;top:1936px;width:311px;height:212px;background:linear-gradient(135deg,#a7a9ab,#8f9193 50%,#5e7e3a)" role="img" aria-label="Curved paved path with bark mulch and conifers"></div>
<div class="photo" style="left:445px;top:2168px;width:311px;height:401px;background:linear-gradient(180deg,#7aa84a,#4f9b2a 40%,#6bc43a 100%)" role="img" aria-label="Bright lawn with stepping stones beside a veranda"></div>
<div class="photo" style="left:445px;top:2589px;width:311px;height:314px;background:linear-gradient(180deg,#8fa6a0,#4f8f33 35%,#5ea83a 100%)" role="img" aria-label="Lawn with stepping stones and curved paved edging"></div>
<div class="photo" style="left:777px;top:1936px;width:311px;height:375px;background:linear-gradient(180deg,#b8c7c4,#8c7f74 35%,#d8cdb9 55%,#5f9a35 80%)" role="img" aria-label="Cottage with flower beds and a green lawn"></div>
<div class="photo" style="left:777px;top:2333px;width:311px;height:375px;background:linear-gradient(180deg,#e9eaea,#6f9a3e 35%,#b8b9b8 60%,#9c9d9c)" role="img" aria-label="Stone steps with potted plant leading to a lawn terrace"></div>

<!-- footer -->
<footer class="abs footer"></footer>
<div class="abs f-brand"><span class="mark"></span>WATTLE</div>
<span class="abs f-social" style="left:165px"></span>
<span class="abs f-social" style="left:195px"></span>
<span class="abs f-social" style="left:228px"></span>

<div class="abs f-head" style="left:367px">Our Office Address</div>
<svg class="abs" style="left:367px;top:3124px" width="13" height="13" viewBox="0 0 24 24"><path d="M6 2 L10 2 L12 8 L9 10 Q12 15 14 15 L16 12 L22 14 L22 18 Q20 22 16 21 Q4 17 3 6 Q3 2 6 2 Z" fill="#fff"/></svg>
<div class="abs f-item" style="left:393px;top:3121px"><b>Phone</b>0203 555 0142</div>
<svg class="abs" style="left:366px;top:3174px" width="15" height="11" viewBox="0 0 15 11"><rect width="15" height="11" rx="1" fill="#fff"/><path d="M1 1 L7.5 6 L14 1" stroke="#093731" stroke-width="1.3" fill="none"/></svg>
<div class="abs f-item" style="left:393px;top:3173px"><b>Email</b>office@wattlelandscaping.example</div>
<svg class="abs" style="left:369px;top:3228px" width="10" height="14" viewBox="0 0 10 14"><path d="M5 0 A5 5 0 0 1 10 5 Q10 8 5 14 Q0 8 0 5 A5 5 0 0 1 5 0 Z" fill="#fff"/><circle cx="5" cy="5" r="2" fill="#093731"/></svg>
<div class="abs f-item" style="left:393px;top:3225px;width:230px"><b>Location</b>Lorem ipsum dolor sit aconsectetur adipiscing elit, sed do eiusmod</div>

<div class="abs f-head" style="left:672px">Company</div>
<div class="abs f-links">Home<br>About Us<br>Services<br>Blog<br>Gallery<br>Contact Us</div>

<div class="abs f-head" style="left:862px">Stil have questios?</div>
<p class="abs f-note">Contact us using this form. A repesenta-tive will aswer your questions as soon as possible.</p>
<div class="abs btn-quote">GET A QUOTE</div>
<div class="abs go-up"><svg width="9" height="9" viewBox="0 0 10 10"><path d="M5 1 L9 6 H6 V9 H4 V6 H1 Z" fill="#fff"/></svg>Go Up</div>
<div class="abs f-rule"></div>
<div class="abs copy">© 2021 Wattle Landscaping | All Rights Reserved</div>
<div class="abs legal">Privacy Policy &nbsp;|&nbsp; Cookie Policy &nbsp;|&nbsp; Terms Of Services</div>

</body>
</html>
```